Redesign of Business Card to look more professional and stand out

Business card design. You can lean more about our company by going to dkrfabworks.example. Raised letters would be nice. Company name & Address
DK&R
418 Wendlow Ridge Drive, Suite 340
Carvel Springs, AL 35199

You can use my name and title: Glenn Harwick
Business Development Manager

Target Market(s)

Heavy Industrial market, i.e. utilities, chemical plants, paper mills, construction companies

Industry/Entity Type

Construction

Contact Information for Business Card

We provide Project Management & Project Support Services

Font styles to use
Serif

Requirements
Must have
• Company name & Address
• DK&R
• 418 Wendlow Ridge Drive, Suite 340
• Carvel Springs, AL 35199
Nice to have
• ideas for the back of the card
Should not have
• no crazy colors. needs to look professional and standout.

```html
<!DOCTYPE html>
<html lang="en">
<head>
<meta charset="utf-8">
<title>DK&amp;R Business Card</title>
<link href="https://fonts.googleapis.com/css2?family=Source+Sans+3:wght@400;700&display=swap" rel="stylesheet">
<style>
  :root {
    --navy: #1f3a6b;
    --navy-deep: #1a3260;
    --ink: #2b2b2b;
    --paper: #ffffff;
    --watermark: #f1f0f3;
    --backdrop: #e9e7e3;
  }
  * { margin: 0; padding: 0; box-sizing: border-box; }
  html, body { width: 1200px; height: 900px; overflow: hidden; }
  body {
    background: var(--backdrop);
    font-family: "Source Sans 3", sans-serif;
    position: relative;
  }
  .card {
    position: absolute;
    width: 520px;
    height: 297px;
    overflow: hidden;
    box-shadow: 0 6px 18px rgba(0,0,0,0.18);
  }
  .card-back {
    left: 70px; top: 170px;
    background: var(--navy-deep);
    display: flex; align-items: center; justify-content: center;
  }
  .card-back .brand-name {
    color: var(--paper);
    font-weight: 700;
    font-size: 120px;
    letter-spacing: 2px;
    line-height: 1;
  }
  .card-front {
    left: 610px; top: 430px;
    background: var(--paper);
  }
  .card-front .watermark {
    position: absolute;
    left: 150px; top: 120px;
    color: var(--watermark);
    font-weight: 700;
    font-size: 200px;
    line-height: 1;
    white-space: nowrap;
    z-index: 0;
  }
  .card-front .brand-name {
    position: absolute;
    left: 36px; top: 34px;
    color: var(--navy);
    font-weight: 700;
    font-size: 72px;
    line-height: 1;
    letter-spacing: 1px;
    z-index: 1;
  }
  .contact {
    position: absolute;
    left: 262px; top: 112px;
    color: var(--ink);
    font-size: 14px;
    line-height: 1.35;
    z-index: 1;
  }
  .contact .person-name {
    color: var(--navy);
    font-weight: 700;
    font-size: 17px;
  }
  .contact .address { margin-top: 22px; }
  .contact .web {
    margin-top: 18px;
    display: flex; align-items: center; gap: 10px;
  }
  .contact .web svg { width: 12px; height: 12px; }
</style>
</head>
<body>
  <section class="card card-back" aria-label="Card back">
    <div class="brand-name">DK&amp;R</div>
  </section>

  <section class="card card-front" aria-label="Card front">
    <div class="watermark" aria-hidden="true">DK&amp;R</div>
    <div class="brand-name">DK&amp;R</div>
    <div class="contact">
      <div class="person-name">Glenn Harwick</div>
      <div class="job-title">Business Development Manager</div>
      <div class="address">
        418 Wendlow Ridge Drive, Suite 340<br>
        Carvel Springs, AL 35199
      </div>
      <div class="web">
        <svg viewBox="0 0 12 12" aria-hidden="true">
          <circle cx="6" cy="6" r="5.5" fill="var(--navy)"/>
          <path d="M1 6h10M6 0.5c-2 2.5-2 8.5 0 11M6 0.5c2 2.5 2 8.5 0 11" stroke="#fff" stroke-width="0.8" fill="none"/>
        </svg>
        <span>www.dkrfabworks.example</span>
      </div>
    </div>
  </section>
</body>
</html>
```